Tails of Comfort Therapy & Dog Training

I have a dual themed business. I am a nationally recognized dog trainer for NHF (National Hound Federation) and Animal Allies (Pet Therapy). One side of my business card will need to address my pet therapy ministry called "Tails of Comfort Therapy". We visit almost 1,000 people a month bringing emotionally uplifting happy visits for nursing homes, veterans hospitals, hospice care, surgery recovery, school systems, and libraries, etc. In addition to emotionally positive effects, pet therapy also helps with anxiety, mobility, regulating blood pressure, and many more advantages. I've attached 2 graphics that are connected with this ministry; #1 paw print inside ribbon heart, #2 clasping hands sketch. The story behind the clasping hands is that it is an actual picture of my hand holding my mother's hand on her death bed (with a sketch filter used). My mother lived in a different state than I live in, and I had wished she had pet therapy available to her in her last months of life. They would have provided some bright moments to her difficult days. So, I vowed that although I was not able to help my own mother, I could train my own dog to reach out to hundreds of people in the community I live in. I have continued to live up to that vow, and have gone on to become a national trainer for other people who would like to train their pets to do the same thing.SIDE TWO of my business card will be announcing that I am a dog trainer for puppies, basic obedience, pet therapy, ESA (emotional support animals), and service dogs. Additionally, I offer canine body language training, dog agility training, and cognitive training. I have also attached two graphics for this side: #1 NHF logo, #2 Animal Allies Evaluation

Target Market(s)

Industry/Entity Type

Dog Training

Contact Information for Business Card

I'm looking for a designer who is good with color scheme & fonts.
2-sided card
one side for pet therapy
one side for dog training

Logo Text

Tails of ComfortTherapy

Font styles to use
Sans Serif
Decorative

Colors

Designer to choose colors to be used in the design.

Requirements
Must have
• -Contact information: Marla Quince (555) 203-9164
• - Contact information for online: Tails of Comfort Therapy (Friendbook, Snapgram & Chirper)
• - Graphics for pet therapy: clasping hands
• - Graphics for dog training: NHF Model Neighbor Dog, Animal Allies
• - List of dog training classes I offer: Basic Obedience, NHF Model Neighbor Dog, NHF B.R.I.G.H.T. Pup, Pet Therapy training, ESA (Emotional Support Animal), Service Dog training, Canine Body Language, Dog Agility, Cognitive Training, Dog Trick Training
Nice to have
• appealing graphic for dog training school
• Titles in decorative font (but still easy to read) & detail info in very easy to read font

```html
<!DOCTYPE html>
<html lang="en">
<head>
<meta charset="utf-8">
<title>Tails of Comfort – Business Cards</title>
<link rel="stylesheet" href="https://fonts.googleapis.com/css2?family=Rye&family=Noticia+Text&display=swap">
<style>
  :root {
    --page: #ffffff;
    --card-light: #fbc95a;
    --card-mid: #f6b43c;
    --card-deep: #f0a22c;
    --ink: #333333;
    --sketch: rgba(120, 90, 40, 0.16);
    --shadow: rgba(0, 0, 0, 0.38);
  }
  * { margin: 0; padding: 0; box-sizing: border-box; }
  html, body {
    width: 1200px;
    height: 1200px;
    overflow: hidden;
    background: var(--page);
  }
  .canvas {
    position: relative;
    width: 1200px;
    height: 1200px;
  }
  .card {
    position: absolute;
    left: 182px;
    width: 836px;
    height: 490px;
    color: var(--ink);
    background:
      repeating-linear-gradient(0deg, rgba(255,255,255,0.05) 0 2px, rgba(0,0,0,0.03) 2px 4px),
      linear-gradient(160deg, var(--card-light) 0%, var(--card-mid) 55%, var(--card-deep) 100%);
    box-shadow: 8px 12px 16px var(--shadow);
    overflow: hidden;
  }
  .card--training { top: 86px; }
  .card--therapy { top: 624px; }

  .card__title {
    position: absolute;
    left: 0;
    top: 0;
    width: 410px;
    height: 240px;
    font-family: "Rye", serif;
    font-weight: 400;
    line-height: 1;
    white-space: nowrap;
  }
  .card__title-main {
    position: absolute;
    left: 44px;
    top: 34px;
    font-size: 94px;
  }
  .card__title-main .initial { font-size: 168px; }
  .card__title-sub {
    position: absolute;
    left: 140px;
    top: 172px;
    font-size: 38px;
  }
  .card__title-sub .initial { font-size: 56px; }
  .card--therapy .card__title-sub { left: 118px; font-size: 40px; }
  .card--therapy .card__title-sub .initial { font-size: 60px; }

  .card__name {
    position: absolute;
    left: 64px;
    top: 388px;
    font-family: "Rye", serif;
    font-size: 28px;
    line-height: 1;
    white-space: nowrap;
  }
  .card__name .initial { font-size: 36px; }

  .card__divider {
    position: absolute;
    left: 418px;
    top: 52px;
    width: 4px;
    height: 402px;
    background: var(--ink);
  }

  .card__sketch {
    position: absolute;
    left: 424px;
    top: 140px;
    width: 370px;
    height: 340px;
    border-radius: 45%;
    background: radial-gradient(ellipse at center, var(--sketch) 0%, rgba(120,90,40,0.06) 60%, transparent 75%);
  }

  .card__details,
  .card__services {
    position: absolute;
    left: 460px;
    width: 340px;
    font-family: "Noticia Text", serif;
    font-size: 20px;
    line-height: 27px;
  }
  .card__details { top: 80px; }
  .card__services { top: 212px; }
</style>
</head>
<body>
<main class="canvas">

  <section class="card card--training">
    <div class="card__sketch" role="img" aria-label="Faint line sketch of a sitting dog"></div>
    <h1 class="card__title">
      <span class="card__title-main"><span class="initial">D</span>OG</span>
      <span class="card__title-sub"><span class="initial">T</span>RAINING</span>
    </h1>
    <p class="card__name"><span class="initial">M</span>ARLA <span class="initial">Q</span>UINCE</p>
    <div class="card__divider"></div>
    <p class="card__details">(555) 203-9164<br>Tails of Comfort Therapy<br>(Friendbook, Snapgram &amp; Chirper)</p>
    <p class="card__services">Basic Obedience, NHF Model Neighbor Dog, NHF B.R.I.G.H.T. Pup, Pet Therapy training, ESA (Emotional Support Animal), Service Dog training, Canine Body Language, Dog Agility, Cognitive Training, Dog Trick Training</p>
  </section>

  <section class="card card--therapy">
    <div class="card__sketch" role="img" aria-label="Faint sketch of two clasped hands"></div>
    <h1 class="card__title">
      <span class="card__title-main"><span class="initial">P</span>ET</span>
      <span class="card__title-sub"><span class="initial">T</span>HERAPY</span>
    </h1>
    <p class="card__name"><span class="initial">M</span>ARLA <span class="initial">Q</span>UINCE</p>
    <div class="card__divider"></div>
    <p class="card__details">(555) 203-9164<br>Tails of Comfort Therapy<br>(Friendbook, Snapgram &amp; Chirper)</p>
    <p class="card__services">Basic Obedience, NHF Model Neighbor Dog, NHF B.R.I.G.H.T. Pup, Pet Therapy training, ESA (Emotional Support Animal), Service Dog training, Canine Body Language, Dog Agility, Cognitive Training, Dog Trick Training</p>
  </section>

</main>
</body>
</html>
```